Design a Banner for Cutest Baby Contest

We are launching a cute baby contest at Velvet Nest dot com. I need a 600x400 Banner for advertising our contest. This needs to include stock baby photos (2 years and younger). Nice graphics that fit our website site theme of green, yellow and brown. Looking for a clean unique design of this banner. Animation ok, I need the jpg, gif and psd photoshop format file with all the layers.

I need 4 600x400 banners for each season:
- Cutest Baby of the Winter Contest
- Cutest Baby of the Spring Contest
- Cutest Baby of the Summer Contest
- Cutest Baby of the Fall Contest

- each season should have a theme for that season...so for winter, do like snowflakes, etc.
- each banner should say Babies only (2 years or younger) in small font with ENTER CONTEST NOW button.
- each banner should say $50 gift card to the winner with most votes.

- I also need a copy of these banners with ENTER CONTEST NOW words taken out and replaced with : CLICK HERE TO VOTE - flashing
Attached is our logo that should be in all the banners in smaller size.

```html
<!DOCTYPE html>
<html lang="en">
<head>
<meta charset="utf-8">
<title>Cutest Baby of the Fall – Velvet Nest</title>
<link rel="stylesheet" href="https://fonts.googleapis.com/css2?family=Anton&family=Roboto+Condensed:wght@400;700&family=Yellowtail&display=swap">
<style>
  :root {
    --amber-deep: #b9480f;
    --amber: #e8862c;
    --gold: #f6c445;
    --cream: #fff8e6;
    --bokeh-light: #f4d9a6;
    --bokeh-mid: #d9a667;
    --fox-orange: #e4621b;
    --fox-dark: #9c3a0c;
    --skin: #f1d2bd;
    --ink: #3a1703;
    --button-top: #ff6a2b;
    --button-bottom: #d8360f;
    --white: #ffffff;
  }
  * { margin: 0; padding: 0; box-sizing: border-box; }
  html, body { width: 1200px; height: 800px; overflow: hidden; background: #fff; }
  .banner {
    position: relative;
    width: 1200px;
    height: 800px;
    overflow: hidden;
    font-family: "Roboto Condensed", sans-serif;
  }
  .autumn-backdrop {
    position: absolute; inset: 0;
    background:
      radial-gradient(circle at 300px 120px, var(--cream) 0, rgba(255,248,230,0) 320px),
      radial-gradient(circle at 80px 420px, var(--amber-deep) 0, rgba(185,72,15,0) 260px),
      radial-gradient(circle at 200px 700px, var(--amber) 0, rgba(232,134,44,0) 300px),
      linear-gradient(100deg, var(--bokeh-mid) 0%, var(--bokeh-light) 45%, #c99a6a 70%, #8c6a4a 100%);
  }
  .baby-photo {
    position: absolute; left: 540px; top: 0; width: 660px; height: 800px;
    background:
      radial-gradient(ellipse 180px 200px at 380px 400px, var(--skin) 0, rgba(241,210,189,0.9) 60%, rgba(241,210,189,0) 100%),
      radial-gradient(ellipse 360px 440px at 380px 380px, var(--fox-orange) 0, #d55a18 70%, rgba(213,90,24,0) 100%),
      linear-gradient(180deg, rgba(228,98,27,0) 60%, var(--fox-dark) 100%);
  }
  .photo-contest {
    position: absolute; left: 20px; top: 112px; width: 570px;
    text-align: center; white-space: nowrap;
    font-family: "Yellowtail", cursive;
    font-weight: 400;
    font-size: 92px; line-height: 1.1;
    color: var(--gold);
    text-shadow: 3px 3px 0 var(--ink), -2px -2px 0 var(--ink), 2px -2px 0 var(--ink), -2px 2px 0 var(--ink), 0 6px 10px rgba(0,0,0,0.45);
  }
  .headline {
    font-family: "Anton", sans-serif;
    font-weight: 400;
    text-transform: uppercase;
  }
  .headline span {
    position: absolute;
    white-space: nowrap;
    line-height: 1;
    transform: skewX(-8deg);
    color: var(--white);
    text-shadow: 3px 3px 0 var(--ink), -3px -3px 0 var(--ink), 3px -3px 0 var(--ink), -3px 3px 0 var(--ink), 0 8px 12px rgba(0,0,0,0.5);
  }
  .headline .line-one { left: 30px; top: 278px; font-size: 104px; }
  .headline .line-two { left: 16px; top: 392px; font-size: 116px; color: var(--gold); }
  .vote-button {
    position: absolute; left: 10px; top: 566px; width: 566px; height: 110px;
    border-radius: 12px;
    border: 3px solid var(--cream);
    background: linear-gradient(180deg, var(--button-top), var(--button-bottom));
    box-shadow: 0 6px 14px rgba(0,0,0,0.4);
    text-align: center; color: var(--white);
    text-decoration: none;
  }
  .vote-button .label {
    display: block; padding-top: 10px;
    font-family: "Anton", sans-serif; font-size: 56px; line-height: 1;
    white-space: nowrap;
    text-shadow: 2px 2px 0 var(--ink);
  }
  .vote-button .eligibility {
    display: block; margin-top: 6px;
    font-weight: 400; font-size: 24px; letter-spacing: 1px;
    white-space: nowrap;
  }
  .prize {
    position: absolute; left: 16px; top: 694px; width: 470px;
    font-family: "Anton", sans-serif; text-transform: uppercase;
    font-size: 36px; line-height: 1.25; color: var(--white);
    white-space: nowrap;
    text-shadow: 2px 2px 0 var(--ink), -2px -2px 0 var(--ink), 2px -2px 0 var(--ink), -2px 2px 0 var(--ink);
  }
  .prize .amount { color: var(--gold); }
  .brand {
    position: absolute; left: 490px; top: 604px; width: 340px;
    text-align: center; color: var(--white);
  }
  .brand-mark { display: block; margin: 0 auto 8px; }
  .brand-name {
    display: block;
    font-family: "Roboto Condensed", sans-serif; font-weight: 400;
    font-size: 38px; letter-spacing: 1px; text-transform: uppercase;
    white-space: nowrap;
  }
</style>
</head>
<body>
<main class="banner">
  <div class="autumn-backdrop" role="img" aria-label="Soft blurred autumn background with orange fall leaves on the left"></div>
  <div class="baby-photo" role="img" aria-label="Smiling baby wearing an orange fox costume hood"></div>

  <h2 class="photo-contest">Photo Contest</h2>

  <h1 class="headline">
    <span class="line-one">Cutest Baby</span>
    <span class="line-two">of the Fall</span>
  </h1>

  <a class="vote-button" href="#vote">
    <span class="label">CLICK HERE TO VOTE</span>
    <span class="eligibility">BABIES ONLY (2 YEARS OR YOUNGER)</span>
  </a>

  <p class="prize">Get the most votes<br>and win <span class="amount">$50 giftcard</span></p>

  <div class="brand">
    <svg class="brand-mark" width="96" height="96" viewBox="0 0 96 96" aria-hidden="true">
      <circle cx="48" cy="48" r="44" fill="none" stroke="var(--white)" stroke-width="3"/>
    </svg>
    <span class="brand-name">Velvet Nest</span>
  </div>
</main>
</body>
</html>
```